Redesign This Psychology Website

We would like a slight redesign of this successful psychology (relationship counselling) website:

www.TheWillowNook.com.au

We are updating the website, and we'd like a slight refresh of the design and style.

Please keep to very similar colours, and use the same logo. We're looking for around 10 page templates, however the main one is the home page.

Keep in mind, this website already converts quite well, so we want a new, fresh design in keeping with this one. Please don't bother designing something too extremely different.

thanks :)

Target Market(s)

couples who are looking for relationship counselling. Men and women, 25 - 70, across Australia

Industry/Entity Type

Psychology

Number of Pages Required

5+ page

Font styles to use
Sans Serif

Colors
87cfc6
b7a5cd
ec1f27
ffffff
cee9f5

Requirements
Must have
• a similar look to the current design, just looking for a slight refresh.
• Search bar
• Areas for lots of photos
• same logo
• lots of content areas
Nice to have
• great content areas, where we can display a lot of content and our areas.
Should not have
• no colors like orange, etc.
• should not have a totally different feel.

```html
<!DOCTYPE html>
<html lang="en">
<head>
<meta charset="utf-8">
<title>The Willow Nook – Relationship &amp; Marriage Counselling</title>
<link href="https://fonts.googleapis.com/css2?family=Open+Sans:ital,wght@0,300;0,400;0,600;0,700;0,800;1,600;1,700&display=swap" rel="stylesheet">
<style>
:root{
  --red:#ec1f27;
  --red-dark:#c4141b;
  --teal:#87cfc6;
  --lavender:#b7a5cd;
  --sky:#cee9f5;
  --white:#ffffff;
  --ink:#2b2b2b;
  --grey:#666;
  --line:#dcdcdc;
}
*{box-sizing:border-box;margin:0;padding:0}
html,body{width:1200px;height:4086px;overflow:hidden}
body{font-family:"Open Sans",Arial,sans-serif;color:var(--ink);background:var(--white);font-size:15px;line-height:1.5}
a{color:inherit;text-decoration:none}
.wrap{width:1090px;margin:0 auto;position:relative}

.utility{height:28px;border-bottom:1px solid var(--line);font-size:12px;text-transform:uppercase;color:var(--grey)}
.utility .wrap{display:flex;justify-content:space-between;height:28px;align-items:center}
.utility nav a{margin-right:20px}
.utility nav a.on{background:var(--red);color:var(--white);padding:6px 12px;font-weight:700}
.utility .util-right a{margin-left:14px}
.utility .util-right a+a{border-left:1px solid var(--line);padding-left:14px}

.header{height:162px}
.header .wrap{display:flex;justify-content:space-between;align-items:center;height:162px}
.brand{display:flex;align-items:center;gap:18px}
.brand-dot{width:92px;height:92px;border-radius:50%;background:var(--teal)}
.brand-name{font-size:46px;font-weight:600;color:var(--teal);line-height:1}
.brand-tag{font-size:20px;color:var(--teal);margin-top:6px;display:block}
.header-tools{text-align:right}
.tool-row{display:flex;justify-content:flex-end;align-items:center;gap:10px}
.social{width:30px;height:30px;border-radius:50%;background:var(--lavender)}
.chip{border:1px solid var(--line);font-size:12px;padding:4px 12px;text-transform:uppercase;color:var(--grey);display:flex;align-items:center;gap:6px}
.call{font-size:30px;color:var(--grey);margin:10px 0 6px;letter-spacing:.5px}
.call strong{color:var(--teal);font-weight:700}
.site-search{display:flex;justify-content:flex-end}
.site-search span{background:var(--lavender);color:var(--white);font-size:13px;font-weight:700;padding:8px 14px}
.site-search div{border:1px solid var(--line);width:268px;font-size:13px;color:#999;padding:8px 12px;text-align:left}

.mainnav{background:var(--red);height:56px}
.mainnav .wrap{display:flex;height:56px;align-items:stretch}
.mainnav a{color:var(--white);font-weight:700;font-size:16px;text-transform:uppercase;padding:0 17px;display:flex;align-items:center}
.mainnav a.on{border-bottom:4px solid var(--white)}

.hero{height:466px;position:relative;background:linear-gradient(180deg,#a9c4d8 0%,#d9c79a 55%,#b8924f 100%)}
.hero-photo{position:absolute;inset:0}
.hero-caption{position:absolute;left:0;top:128px;background:rgba(60,60,60,.72);color:var(--white);padding:22px 40px 26px 55px;width:590px}
.hero-caption p{font-size:32px;font-weight:300}
.hero-caption h1{font-size:37px;font-weight:800;text-transform:uppercase;line-height:1.25;white-space:nowrap}
.hero-arrow{position:absolute;top:216px;width:20px;height:34px;color:var(--white)}

.welcome{text-align:center;padding:34px 0 40px}
.welcome h2{font-size:46px;font-weight:300}
.welcome h2 strong{font-weight:700}
.welcome p{font-size:24px;color:var(--grey);font-weight:300}

.services{display:grid;grid-template-columns:repeat(4,1fr);gap:26px}
.service{border:2px solid var(--sky);text-align:center;height:534px;display:flex;flex-direction:column}
.service-photo{height:175px;margin:10px 10px 0;background:linear-gradient(180deg,#f2f2f2,#d9d3cc)}
.service h3{background:var(--sky);font-size:16px;font-weight:800;text-transform:uppercase;line-height:1.25;padding:8px 10px;margin:0 0 14px}
.service .ask{font-size:15px;color:var(--grey)}
.service .needs{font-size:15px;padding:18px 18px 0;line-height:1.45;min-height:150px}
.service .extra{font-size:15px;line-height:1.6}
.btn{display:inline-block;background:var(--red);color:var(--white);font-weight:700;font-size:15px;text-transform:uppercase;padding:5px 22px;border-radius:4px;border-bottom:3px solid var(--red-dark)}
.service .btn{margin:auto auto 20px}

.finder{background:var(--red);margin-top:40px;height:182px;color:var(--white);text-align:center;padding-top:28px}
.finder h2{font-size:27px;font-weight:700;text-transform:uppercase}
.finder-form{display:flex;justify-content:center;align-items:center;gap:14px;margin-top:28px}
.field{background:var(--white);color:#888;font-size:14px;height:40px;padding:9px 16px;text-align:left}
.finder .or{font-size:22px;font-weight:700;margin:0 10px}
.finder .go{background:#3a0a0c;font-weight:700;font-size:16px;height:40px;padding:8px 30px;text-transform:uppercase}

.content{display:flex;gap:30px;padding-top:40px}
.main{width:780px}
.aside{width:280px}
.main h2{font-size:29px;font-weight:400;margin-bottom:22px}
.main h2 strong{font-weight:700}
.main h3{font-size:25px;font-weight:800;margin:36px 0 18px;white-space:nowrap}
.main p{font-size:15.5px;margin-bottom:18px}
.main .hl{color:var(--red);font-weight:700}
.video{width:670px;height:376px;margin:26px 0 30px;background:linear-gradient(135deg,#e9eef2,#c4ccd3);position:relative}
.play{position:absolute;left:50%;top:50%;width:90px;height:62px;margin:-31px 0 0 -45px}
.issues{display:grid;grid-template-columns:1fr 1fr;gap:0 30px;list-style:none;font-size:15.5px;margin-top:8px}
.issues li,.locations li{padding-left:26px;position:relative;line-height:2.05}
.issues li::before,.locations li::before{content:"";position:absolute;left:4px;top:13px;width:8px;height:8px;border-radius:50%;background:var(--ink)}
.promo-pair{display:flex;gap:22px;margin:30px 0 10px}
.promo{border:9px solid var(--teal);width:350px;height:150px;display:flex;align-items:center;gap:16px;padding-right:16px}
.promo-photo{width:150px;height:132px;background:linear-gradient(180deg,#dfe9ee,#c8b8a8)}
.promo p{font-size:19px;font-style:italic;font-weight:600;margin:0;line-height:1.3}
.promo p span{color:var(--red);display:block}
.locations{display:grid;grid-template-columns:1fr 1fr;list-style:none;font-size:15.5px;width:560px;margin:6px 0 18px}
.locations b{font-weight:700}
.main a.inline{color:var(--red);text-decoration:underline;font-style:italic}

.ad{border:1px solid var(--line);margin-bottom:24px;position:relative;display:block}
.ad-strip{background:var(--red);color:var(--white);font-size:12.5px;font-weight:600;padding:4px 10px}
.ad-strip.teal{background:var(--teal)}
.ad-anxiety{height:212px;background:linear-gradient(90deg,#fff 40%,#f1dcd3)}
.ad-anxiety h4{color:var(--red);font-size:21px;font-style:italic;font-weight:700;line-height:1.2;padding:14px 12px 0;width:150px}
.ad-anxiety .ad-strip,.ad-gp .ad-strip{position:absolute;bottom:0;left:0;right:0}
.ad-gp{height:168px;background:linear-gradient(90deg,#d4e7f4,#fff 55%)}
.ad-gp h4{position:absolute;right:12px;top:40px;width:130px;font-size:17px;font-style:italic;font-weight:700;line-height:1.2}
.ad-rebate h4{color:var(--red);font-weight:700;font-size:17px;padding:8px 10px 6px}
.badges{display:grid;grid-template-columns:repeat(3,1fr);gap:8px;padding:0 10px}
.badge{height:30px;border-radius:3px;background:var(--sky)}
.badge.alt{background:var(--lavender)}
.badge.tiny{height:24px;background:#e6e6e6}
.more{color:var(--red);text-align:center;font-size:13px;font-weight:700;font-style:italic;margin:6px 0}
.ad-rebate p{font-size:15px;color:var(--grey);padding:0 10px 10px;line-height:1.35}
.ad-rebate p b{color:var(--red)}
.ad-video .shot{height:188px;background:linear-gradient(180deg,#c9b6a4,#8a6e5c);position:relative}
.blog-head{font-size:19px;margin:34px 0 0}
.blog-head strong{display:block;color:var(--red);font-size:26px;font-weight:700;line-height:1.3}
.blog-feature{height:112px;margin:14px 0 10px;background:linear-gradient(180deg,#f4f4f4,#dedad4)}
.post{border:2px solid var(--sky);display:flex;gap:12px;padding:12px;margin-bottom:16px;height:160px}
.post-photo{width:92px;height:112px;flex:none;background:linear-gradient(180deg,#d9d2ca,#9d8b7c)}
.post h5{color:var(--red);font-size:15px;font-style:italic;font-weight:700;line-height:1.25}
.post time{display:block;font-size:12.5px;color:var(--grey);margin:2px 0 8px}
.post .btn{font-size:13px;padding:3px 14px}
</style>
</head>
<body>

<div class="utility">
  <div class="wrap">
    <nav><a class="on" href="#">Home</a><a href="#">About</a><a href="#">Resources</a><a href="#">Blog</a></nav>
    <div class="util-right"><a href="#">Join our Associate Program</a><a href="#">Marriage Counselling</a><a href="#">Relationship Counselling</a></div>
  </div>
</div>

<header class="header">
  <div class="wrap">
    <a class="brand" href="#">
      <span class="brand-dot"></span>
      <span><span class="brand-name">The Willow Nook</span><span class="brand-tag">helping you create loving relationships</span></span>
    </a>
    <div class="header-tools">
      <div class="tool-row">
        <span class="social"></span><span class="social"></span><span class="social"></span>
        <span class="chip">Shop</span>
        <span class="chip"><svg width="14" height="12" viewBox="0 0 14 12"><path d="M0 1h2.5l2 7h7l2-5.5H4" fill="none" stroke="#666" stroke-width="1.4"/><circle cx="5.5" cy="10.5" r="1.2" fill="#666"/><circle cx="10.5" cy="10.5" r="1.2" fill="#666"/></svg>Cart (0)</span>
      </div>
      <div class="call">CALL US ON <strong>1300 555 019</strong></div>
      <div class="site-search"><span>SEARCH</span><div>Relationship Information Topic</div></div>
    </div>
  </div>
</header>

<nav class="mainnav">
  <div class="wrap">
    <a class="on" href="#">Counselling Types</a>
    <a href="#">Relationship Counselling Locations</a>
    <a href="#">Sex Therapy Locations</a>
    <a href="#">Quizzes</a>
    <a href="#">FAQ's</a>
    <a href="#">Contact</a>
  </div>
</nav>

<section class="hero">
  <div class="hero-photo" role="img" aria-label="Photo of a happy couple embracing in a golden field"></div>
  <div class="hero-caption">
    <p>We Specialise in</p>
    <h1>Relationship &amp;<br>Marriage Counselling</h1>
  </div>
  <svg class="hero-arrow" style="left:14px" viewBox="0 0 20 34"><path d="M16 3L4 17l12 14" fill="none" stroke="currentColor" stroke-width="4"/></svg>
  <svg class="hero-arrow" style="right:14px" viewBox="0 0 20 34"><path d="M4 3l12 14L4 31" fill="none" stroke="currentColor" stroke-width="4"/></svg>
</section>

<section class="welcome">
  <h2>Welcome to <strong>The Willow Nook</strong></h2>
  <p>Our team of 75 hand chosen Registered Psychologists in 81 locations Australia wide</p>
</section>

<section class="wrap services">
  <article class="service">
    <div class="service-photo" role="img" aria-label="Photo of a couple sitting apart, looking upset"></div>
    <h3>Relationship<br>Counselling</h3>
    <p class="ask">Do you need help with:</p>
    <p class="needs">Communication, Recovering from an affair, Loss of intimacy &amp; love, Power battles, Feeling like friends, not lovers</p>
    <p class="extra">Take our Relationship Quiz<br>Pre-marriage</p>
    <a class="btn" href="#">More</a>
  </article>
  <article class="service">
    <div class="service-photo" role="img" aria-label="Photo of a couple in bed"></div>
    <h3>Sex Therapy<br>Counselling</h3>
    <p class="ask">Do you need help with:</p>
    <p class="needs">Low libido , Erectile difficulties, Premature ejaculation, Differing libidos, Porn addiction, Keeping sex exciting</p>
    <p class="extra">Take Sex Quiz</p>
    <a class="btn" href="#">More</a>
  </article>
  <article class="service">
    <div class="service-photo" role="img" aria-label="Photo of an angry man"></div>
    <h3>Anger Management<br>Counselling</h3>
    <p class="ask">Do you need help with:</p>
    <p class="needs">Managing angry outbursts, expressing your anger in healthy ways</p>
    <p class="extra">Take our Anger Test</p>
    <a class="btn" href="#">More</a>
  </article>
  <article class="service">
    <div class="service-photo" role="img" aria-label="Photo of a woman admiring herself"></div>
    <h3>Narcissism<br>Counselling</h3>
    <p class="ask">Do you need help with:</p>
    <p class="needs">Managing narcissistic, superior, entitled, arrogant and lack of empathy tendencies in you or your partner</p>
    <p class="extra">Check your Narcissism Profile</p>
    <a class="btn" href="#">More</a>
  </article>
</section>

<section class="finder">
  <h2>Find our Psychologist near you</h2>
  <div class="finder-form">
    <div class="field" style="width:370px">Type of Counselling</div>
    <div class="field" style="width:270px">Location</div>
    <span class="or">OR</span>
    <div class="field" style="width:160px">Postcode</div>
    <span class="go">Search</span>
  </div>
</section>

<div class="wrap content">
  <main class="main">
    <h2>We Specialise in <strong>Relationship &amp; Marriage Counselling</strong></h2>
    <p>At The Willow Nook, we are a group of <b>PSYCHOLOGISTS</b>, Australia wide who are <b>passionate about relationships and helping you with yours.</b></p>
    <p>Our vision is to provide the <b>most highly regarded and comprehensive <span class="hl">marriage counselling</span> and <span class="hl">relationship counselling</span>,</b> and <span class="hl">sex therapy</span> in Australia, at reasonable and affordable rates.</p>
    <p>When we are experiencing relationship and marriage problems, there can be a lot of pain and confusion, and it can often be difficult to cope with the other areas of our lives when we are struggling with problems with our partner.</p>
    <p>We are not taught about relationships and how to have a good one in our schools, so most of us are doing the best we know how, but lack the knowledge on how to create a better relationship.</p>

    <div class="video" role="img" aria-label="Video still of a smiling psychologist introducing the practice">
      <svg class="play" viewBox="0 0 90 62"><rect width="90" height="62" rx="12" fill="#2b2b2b" opacity=".85"/><path d="M36 18l22 13-22 13z" fill="#fff"/></svg>
    </div>

    <h3>Our Willow Nook Psychologists</h3>
    <p>Our team of 75 hand chosen Registered Psychologists in 81 locations Australia wide, are individually selected for their knowledge, experience, compassion, and unbiased approach to marriage counselling and sexual therapy.</p>
    <p>In addition all our Psychologists take part in our Initial Relationship Counselling Methodologies Training and yearly in-house conferences, ensuring you are in safe and experienced hands.</p>
    <p>As we are Psychologists, you may be eligible for public health &amp; private health insurance rebates. We are highly experienced and can help you with all kinds of relationship difficulties.</p>
    <p>Here are some of the common ones:</p>
    <ul class="issues">
      <li>Affairs</li><li>Problems from childhood</li>
      <li>Controlling behaviour</li><li>Problems with parenting your children</li>
      <li>Verbal abuse</li><li>Step children and in-laws</li>
      <li>Imbalance of power</li><li>All forms of family problems</li>
      <li>Lack of intimacy</li><li>Anger management problems</li>
      <li>Poor communication</li><li>Porn addiction problems</li>
      <li>Loss of love</li><li>Pre-marriage programs</li>
      <li>Relationship neglect</li><li>Narcissism problems</li>
      <li>Sexual problems</li>
    </ul>

    <h3>Our Relationship Counselling Approach</h3>
    <p>It is an important part of our policy to take a very positive approach to our relationship counselling.</p>
    <p>We feel it is important to really understand the problems and perspectives of each of you, and at the same time, we find that most couples are looking to find a positive action plan and way through their problems to make changes which have a positive impact and a real sense of hope for their relationship.</p>
    <p>Read more about our approach to counselling in our relationship counselling sessions, and frequently asked questions about the relationship and marriage counselling process.</p>

    <div class="promo-pair">
      <a class="promo" href="#"><span class="promo-photo" role="img" aria-label="Photo of a smiling couple"></span><p>Take our<span>Willow Nook Relationship Assessment</span></p></a>
      <a class="promo" href="#"><span class="promo-photo" role="img" aria-label="Photo of a friendly psychologist"></span><p>Find out<span>more about us</span></p></a>
    </div>

    <h3>Our Relationship Counselling Locations across Australia</h3>
    <p>We currently have relationship counselling and marriage counselling services in:</p>
    <ul class="locations">
      <li><b>Sydney</b> – 19 centres</li><li><b>Adelaide</b> – 4 centres</li>
      <li><b>Canberra</b> – 2 centres</li><li><b>Gold Coast</b> – 5 centres</li>
      <li><b>Melbourne</b> – 21 centres</li><li><b>Sunshine Coast</b> – 2 centres</li>
      <li><b>Perth</b> – 11 centres</li><li><b>Cairns</b> – 1 centre</li>
      <li><b>Brisbane</b> – 14 centres</li><li><b>Townsville</b> – 1 centre</li>
      <li><b>Wollongong</b> – 1 centre</li><li><b>Wodonga</b> – 1 centre</li>
      <li><b>Central Coast</b> – 2 centres</li>
    </ul>
    <p>Certain clinics also provide after hours and Saturday sessions for your convenience.</p>
    <p>Click the <a class="inline" href="#">Locations</a> tab for more information about one of our caring psychologists in your area.</p>
  </main>

  <aside class="aside">
    <a class="ad ad-anxiety" href="#" role="img" aria-label="Photo of a worried woman beside an anxiety help banner">
      <h4>Is Anxiety, Depression or Stress bothering YOU?</h4>
      <div class="ad-strip">Click here for help from our Anxiety &amp; Depression Psychologists</div>
    </a>
    <a class="ad ad-gp" href="#" role="img" aria-label="Photo of a doctor beside a referral banner">
      <h4>Information for referring GPs &amp; health professionals</h4>
      <div class="ad-strip teal">Click here for more details.</div>
    </a>
    <div class="ad ad-rebate">
      <h4>Rebates Available</h4>
      <div class="badges">
        <span class="badge"></span><span class="badge alt"></span><span class="badge"></span>
        <span class="badge tiny"></span><span class="badge tiny"></span><span class="badge tiny"></span>
        <span class="badge tiny"></span><span class="badge tiny"></span><span class="badge tiny"></span>
      </div>
      <div class="more">— plus many more —</div>
      <p>You may be able to receive rebates of up to <b>75% of your session costs</b> from public health or private health insurers.</p>
      <div class="ad-strip teal">Click here for more details.</div>
    </div>
    <div class="ad ad-video">
      <div class="ad-strip">What To Expect From Counselling</div>
      <div class="shot" role="img" aria-label="Video still of a couple in a counselling session">
        <svg class="play" viewBox="0 0 90 62" style="width:60px;height:42px;margin:-21px 0 0 -30px"><circle cx="45" cy="31" r="28" fill="#ec1f27"/><path d="M38 19l20 12-20 12z" fill="#fff"/></svg>
      </div>
    </div>

    <h4 class="blog-head">Our selection of blog posts on<strong>Relationships &amp; Sex</strong></h4>
    <div class="blog-feature" role="img" aria-label="Illustration of a couple reaching toward each other"></div>

    <article class="post">
      <div class="post-photo" role="img" aria-label="Portrait photo of a psychologist"></div>
      <div><h5>Relationship Counselling Sydney Psychologist Interview: Sam</h5><time>April 27, 2017</time><a class="btn" href="#">Read More</a></div>
    </article>
    <article class="post">
      <div class="post-photo" role="img" aria-label="Photo of a troubled couple"></div>
      <div><h5>What can I do if I'm living with a Narcissist?</h5><time>February 24, 2017</time><a class="btn" href="#">Read More</a></div>
    </article>
    <article class="post">
      <div class="post-photo" role="img" aria-label="Photo of a woman looking thoughtful"></div>
      <div><h5>Why am I with a Narcissist?</h5><time>February 24, 2017</time><a class="btn" href="#">Read More</a></div>
    </article>
    <article class="post">
      <div class="post-photo" role="img" aria-label="Photo of a couple arguing"></div>
      <div><h5>How Do I Know If I'm With a Narcissist?</h5><time>February 24, 2017</time><a class="btn" href="#">Read More</a></div>
    </article>
    <article class="post">
      <div class="post-photo" role="img" aria-label="Photo of a man shouting"></div>
      <div><h5>Are You Living With a Steamroller?</h5><time>February 10, 2017</time><a class="btn" href="#">Read More</a></div>
    </article>
    <article class="post">
      <div class="post-photo" role="img" aria-label="Photo of a hesitant partner"></div>
      <div><h5>Letter for a Partner Doubtful About Relationship Counselling</h5><time>February 3, 2017</time><a class="btn" href="#">Read More</a></div>
    </article>
  </aside>
</div>

</body>
</html>
```